Japanese Rice Food Package Label

- We are launching Japanese food products to the outdoor community.
- Made in Japan
- We will have multiple flavors of rice but want to keep the package label almost the same and only replace the flavor text (e.g., Mixed Rice, Curry Rice, etc)
- We like simple designs inspired by Japan.
- Label size: 105 mm x148 mm
- Our brand: YURATO https://yurato.co/
- Video message: https://www.clipvane.com/share/4b7e19d0a3c65f2e8d1a7b30c9e5f412

```html
<!DOCTYPE html>
<html lang="en">
<head>
<meta charset="utf-8">
<title>YURATO Curry Rice – Pouch Label</title>
<link rel="stylesheet" href="https://fonts.googleapis.com/css2?family=Montserrat:wght@300;700;800&family=Barlow+Semi+Condensed:wght@400;600&display=swap">
<style>
  :root {
    --page: #ffffff;
    --pouch: #d9d9d9;
    --label-red: #f24346;
    --band-green: #214a47;
    --white: #ffffff;
    --photo-top: #c7b3a0;
    --photo-mid: #e9e2d8;
    --photo-rice: #c99a62;
  }
  html, body {
    margin: 0;
    padding: 0;
    width: 1200px;
    height: 1019px;
    overflow: hidden;
    background: var(--page);
  }
  .pouch-art {
    display: block;
    width: 1200px;
    height: 1019px;
  }
  .brand-name {
    font-family: "Montserrat", sans-serif;
    font-weight: 800;
    fill: var(--white);
  }
  .flavor-name {
    font-family: "Montserrat", sans-serif;
    font-weight: 700;
    fill: var(--white);
  }
  .flavor-sub {
    font-family: "Montserrat", sans-serif;
    font-weight: 300;
    fill: var(--white);
    letter-spacing: 9px;
  }
  .step-title {
    font-family: "Barlow Semi Condensed", sans-serif;
    font-weight: 600;
    font-size: 16px;
    fill: var(--white);
  }
  .step-note {
    font-family: "Barlow Semi Condensed", sans-serif;
    font-weight: 400;
    font-size: 10px;
    fill: var(--white);
  }
  .shelf-title {
    font-family: "Barlow Semi Condensed", sans-serif;
    font-weight: 600;
    font-size: 18px;
    fill: var(--band-green);
  }
  .shelf-note {
    font-family: "Barlow Semi Condensed", sans-serif;
    font-weight: 400;
    font-size: 10px;
    fill: var(--band-green);
  }
  .footer-url {
    font-family: "Barlow Semi Condensed", sans-serif;
    font-weight: 600;
    font-size: 24px;
    letter-spacing: 1px;
    fill: var(--white);
  }
  .footer-origin {
    font-family: "Barlow Semi Condensed", sans-serif;
    font-weight: 600;
    font-size: 19px;
    fill: var(--white);
  }
  .icon-line {
    fill: none;
    stroke: var(--white);
    stroke-width: 2.2;
    stroke-linecap: round;
  }
  .icon-fill { fill: var(--white); }
</style>
</head>
<body>
<svg class="pouch-art" viewBox="0 0 1200 1019" xmlns="http://www.w3.org/2000/svg">
  <defs>
    <linearGradient id="mealPhoto" x1="0" y1="0" x2="0" y2="1">
      <stop offset="0" stop-color="var(--photo-top)"/>
      <stop offset="0.45" stop-color="var(--photo-mid)"/>
      <stop offset="0.75" stop-color="var(--photo-rice)"/>
      <stop offset="1" stop-color="var(--photo-mid)"/>
    </linearGradient>
  </defs>

  <!-- pouch -->
  <g class="pouch">
    <rect x="167" y="106" width="851" height="110" rx="29" fill="var(--pouch)"/>
    <rect x="570" y="131" width="47" height="34" rx="12" fill="var(--page)"/>
    <path d="M167,250 Q167,216 200,216 L987,216 Q1019,216 1019,250 L1019,855 Q1019,880 994,882 L790,899 Q760,902 730,902 L350,902 Q320,902 290,899 L193,882 Q167,878 167,855 Z" fill="var(--pouch)"/>
  </g>

  <!-- label -->
  <g class="label">
    <path d="M213,295 L897,295 Q912,295 922,305 L972,356 Q981,366 981,380 L981,838 Q981,846 973,846 L213,846 Q205,846 205,838 L205,303 Q205,295 213,295 Z" fill="var(--label-red)"/>

    <text class="brand-name" x="277" y="496" font-size="200" textLength="596" lengthAdjust="spacingAndGlyphs">YURATO</text>
    <g class="registered-mark">
      <circle cx="898" cy="369" r="14" fill="none" stroke="var(--white)" stroke-width="3"/>
      <text x="898" y="376" text-anchor="middle" font-family="Montserrat, sans-serif" font-weight="800" font-size="19" fill="var(--white)">R</text>
    </g>

    <text class="flavor-name" x="585" y="567" font-size="65" text-anchor="middle" textLength="407" lengthAdjust="spacingAndGlyphs">CURRY RICE</text>
    <text class="flavor-sub" x="594" y="591" font-size="26" text-anchor="middle" textLength="286">WITH VEGETABLES</text>

    <!-- preparation and shelf-life panel -->
    <g class="info-panel">
      <path d="M669,606 L920,606 Q936,606 936,622 L936,732 Q936,748 920,748 L669,748 Z" fill="var(--white)"/>
      <rect x="255" y="606" width="681" height="142" rx="14" fill="none" stroke="var(--white)" stroke-width="4"/>

      <g class="step step-no-microwave">
        <circle class="icon-line" cx="335" cy="651" r="28"/>
        <rect class="icon-line" x="321" y="642" width="29" height="20" rx="2"/>
        <line class="icon-line" x1="341" y1="642" x2="341" y2="662"/>
        <line class="icon-line" x1="316" y1="632" x2="355" y2="671"/>
        <text class="step-title" x="338" y="713" text-anchor="middle">NO MICROWAVE</text>
        <text class="step-note" x="338" y="733" text-anchor="middle">LOREM IPSUM DOLOR SIT.</text>
      </g>

      <g class="step step-hot-water">
        <path class="icon-fill" d="M442,650 L478,650 L480,670 Q480,674 476,674 L444,674 Q440,674 440,670 Z"/>
        <path class="icon-fill" d="M479,660 L490,650 L493,653 L481,667 Z"/>
        <path class="icon-line" d="M445,648 Q447,630 460,630 Q473,630 475,648"/>
        <circle class="icon-fill" cx="460" cy="641" r="3"/>
        <path class="icon-line" d="M486,638 Q482,643 486,648"/>
        <text class="step-title" x="466" y="714" text-anchor="middle">USE HOT WATER</text>
        <text class="step-note" x="466" y="734" text-anchor="middle">LOREM IPSUM DOLOR SIT.</text>
      </g>

      <g class="step step-shake">
        <rect class="icon-line" x="573" y="638" width="37" height="34" rx="3"/>
        <line class="icon-line" x1="573" y1="644" x2="610" y2="644"/>
        <path class="icon-line" d="M567,667 A30,30 0 0 1 598,628"/>
        <path class="icon-line" d="M614,636 A30,30 0 0 1 585,682"/>
        <path class="icon-fill" d="M563,663 L571,665 L566,671 Z"/>
        <path class="icon-fill" d="M612,632 L620,638 L612,641 Z"/>
        <text class="step-title" x="595" y="705" text-anchor="middle">SHAKE UNTIL</text>
        <text class="step-title" x="595" y="720" text-anchor="middle">REHYDRATED</text>
        <text class="step-note" x="593" y="734" text-anchor="middle">LOREM IPSUM DOLOR SIT.</text>
      </g>

      <rect class="meal-photo" x="674" y="608" width="260" height="107" fill="url(#mealPhoto)" role="img" aria-label="Photo of curry rice with vegetables served in a white bowl"/>

      <text class="shelf-title" x="796" y="737" text-anchor="middle">SHELF LIFE 25 YEARS</text>
      <text class="shelf-note" x="796" y="746" text-anchor="middle">LOREM IPSUM DOLOR SIT.</text>
    </g>

    <!-- footer band -->
    <path class="footer-band" d="M205,769 L981,769 L981,838 Q981,846 973,846 L213,846 Q205,846 205,838 Z" fill="var(--band-green)"/>
    <text class="footer-url" x="593" y="806" text-anchor="middle">WWW.YURATO.CO</text>
    <text class="footer-origin" x="587" y="826" text-anchor="middle">MADE IN JAPAN</text>
  </g>
</svg>
</body>
</html>
```